Tall Pine Construction Need an information and interactive website with client portal. We have ou

Need to have a client log in screen for work orders and estimate requests.
Nice informational landing page.

Tall Pine is a full service general contractor servicing apartment complexes;
maintenance of grounds and apartments - remodeling and construction.

Design Specifics: We are pretty open here. Some good examples are
www.halvexworks.com , lorrenhousing.com and www.quin7renovate.com

For the site we need:
Homepage - to explain services
Roofing page
Apartment Page
Client Portal - where clients can set up accounts to set up work/estimate request that will be routed to our email

--Will need coding, plan to host site on Wordpress

Target Market(s)

Multi family, Residential and commercial clients

Industry/Entity Type

Construction

Coding

Coded - Design and coding required

Number of Pages Required

3 page

Font styles to use
Serif

Requirements
Must have
• Client portal
Nice to have
• Not sure. please advise

```html
<!DOCTYPE html>
<html lang="en">
<head>
<meta charset="utf-8">
<title>Tall Pine Construction — Home</title>
<link href="https://fonts.googleapis.com/css2?family=Ubuntu:wght@400;500;700&family=Montserrat:wght@400;600&family=Playfair+Display:ital,wght@1,400;1,700&display=swap" rel="stylesheet">
<style>
:root{
  --stage:#6b2f2c;
  --red:#c4141a;
  --blue:#1a4fd8;
  --ink:#1d1d1d;
  --muted:#555;
  --paper:#ffffff;
  --mist:#ecebe9;
  --brown:#6f5247;
  --hero-a:#2a3038;
  --hero-b:#4a4e52;
}
*{box-sizing:border-box;margin:0;padding:0}
html,body{width:1200px;height:1200px;overflow:hidden;background:var(--stage)}
.stage{position:absolute;left:0;top:0;width:1500px;height:1500px;transform:scale(.8);transform-origin:0 0}
.page{position:absolute;left:404px;top:0;width:692px;height:1500px;background:var(--paper);font-family:"Montserrat",sans-serif;color:var(--ink);overflow:hidden}
.abs{position:absolute}
.nav a{position:absolute;top:16px;font-size:6.5px;letter-spacing:.3px;color:#fff;text-decoration:none;text-transform:uppercase}
.hero{left:0;top:0;width:692px;height:292px;background:linear-gradient(180deg,#1f252c 0%,var(--hero-a) 35%,var(--hero-b) 100%)}
.logo{left:286px;top:20px;width:120px;text-align:center;font-family:"Ubuntu",sans-serif;font-weight:700;font-size:13px;color:#fff;letter-spacing:1px;display:flex;align-items:center;justify-content:center;gap:5px}
.logo i{display:inline-block;width:8px;height:8px;background:var(--red)}
.tagline{left:0;width:692px;top:122px;text-align:center;font-family:"Playfair Display",serif;font-style:italic;font-size:10px;color:#fff}
.hero-rule{left:276px;top:116px;width:140px;height:1px;background:rgba(255,255,255,.4)}
.headline{left:0;width:692px;top:140px;text-align:center;font-family:"Ubuntu",sans-serif;font-weight:700;font-size:26px;line-height:26px;color:#fff}
.estimate{left:669px;top:145px;width:23px;height:93px;background:var(--red);color:#fff;font-family:"Ubuntu",sans-serif;font-weight:700;font-size:10px;writing-mode:vertical-rl;transform:rotate(180deg);display:flex;align-items:center;justify-content:center}
.h2{font-family:"Ubuntu",sans-serif;font-weight:500;font-size:12.5px;color:var(--ink)}
.body{font-size:6.6px;line-height:14px;color:#444}
.about-text{z-index:2}
.btn{background:var(--red);color:#fff;font-size:6px;display:flex;align-items:center;justify-content:center;text-transform:uppercase}
.about-img{left:353px;top:322px;width:263px;height:153px;background:linear-gradient(90deg,rgba(255,255,255,.85) 0%,rgba(255,255,255,.85) 12%,#c8c9c2 30%,#e5e4dc 70%,#9a9b97 100%)}
.services-band{left:0;top:511px;width:692px;height:162px;background:linear-gradient(90deg,#5c4a35 0%,#b8ad9c 40%,#cfc6b8 60%,#6b5d48 100%)}
.card{top:529px;width:124px;height:128px;background:var(--red);color:#fff;text-align:center}
.card.blue{background:var(--blue)}
.card .ic{position:absolute;left:45px;top:14px;width:34px;height:34px;border-radius:50%;background:#fff;display:flex;align-items:center;justify-content:center}
.card h3{position:absolute;top:53px;width:100%;font-size:6.5px;font-weight:600;line-height:8.5px}
.card p{position:absolute;top:74px;left:6px;right:6px;font-size:5.6px;line-height:10px;opacity:.9}
.card .more{position:absolute;left:7px;right:7px;top:105px;height:13px;border:1px solid rgba(255,255,255,.5);font-size:4.8px;text-align:left;padding:3px 5px;display:flex;justify-content:space-between}
.stat{top:694px;width:200px;text-align:center}
.stat b{display:block;font-family:"Ubuntu",sans-serif;font-weight:700;font-size:22px;color:var(--red)}
.stat span{font-size:7.5px;color:#333}
.vdiv{top:690px;width:1px;height:54px;background:#ddd}
.cats{left:0;top:759px;width:692px;height:76px;display:flex}
.cats div{flex:1;display:flex;align-items:center;justify-content:center;text-align:center;font-size:7px;color:#fff;text-transform:uppercase;line-height:9px;border-right:1px solid rgba(0,0,0,.2)}
.blog{left:0;top:835px;width:692px;height:248px;background:var(--mist)}
.post{top:902px;width:168px;height:146px;background:#fff;box-shadow:0 1px 2px rgba(0,0,0,.15)}
.post .ph{height:56px}
.post h4{position:absolute;left:9px;right:9px;top:66px;font-weight:400;font-size:9px;line-height:12px;color:#333}
.post time{position:absolute;left:9px;top:98px;font-size:6px;color:#555}
.post .rm{position:absolute;left:9px;right:9px;top:124px;height:13px;border:1px solid #ccc;font-size:4.8px;color:#777;padding:3px 4px;display:flex;justify-content:space-between}
.sat{left:0;top:1083px;width:431px;height:280px;background:radial-gradient(ellipse at 60% 70%,#8a5d3e 0%,#4b3226 55%,#2a1d18 100%)}
.sat-kicker{left:76px;top:1119px;font-size:6px;color:#fff}
.sat-title{left:76px;top:1137px;font-family:"Ubuntu",sans-serif;font-size:13.5px;line-height:19px;color:#fff;font-weight:400}
.sat-copy{left:76px;top:1184px;width:280px;font-size:5.6px;line-height:10px;color:#fff}
.say{left:431px;top:1083px;width:185px;height:280px;background:var(--brown);color:#fff;text-align:center}
.sat-right{left:616px;top:1083px;width:76px;height:280px;background:linear-gradient(180deg,#3b2420,#1e1412)}
.foot-nav a{position:absolute;top:1398px;font-size:6.5px;color:#333;text-decoration:none;text-transform:uppercase}
.social{top:1445px;width:14px;height:14px;background:#2b2b2b}
.copy{left:0;top:1480px;width:692px;height:20px;background:#efefef;font-size:5.5px;color:#888;text-align:center;line-height:20px}
</style>
</head>
<body>
<div class="stage">
 <main class="page">
  <header class="abs hero" role="img" aria-label="Photo of a dark modern apartment living room overlooking a city skyline at night"></header>
  <nav class="nav">
   <a style="left:76px">Roofing</a><a style="left:127px">Apartment</a><a style="left:183px">Client Portal</a>
   <a style="left:478px">Services</a><a style="left:524px">Projects</a><a style="left:575px">Contact Us</a>
  </nav>
  <div class="abs logo"><i></i>TALL PINE</div>
  <div class="abs hero-rule"></div>
  <p class="abs tagline">Great Experience in Construction</p>
  <h1 class="abs headline">REMODELING &amp; GENERAL<br>HANDYMAN WORK</h1>
  <div class="abs estimate">GET ESTIMATE</div>

  <section>
   <div class="abs about-img" role="img" aria-label="Photo of a bright minimal interior with a white lounge chair and floor lamp"></div>
   <h2 class="abs h2 about-text" style="left:76px;top:341px">TALL PINE CONSTRUCTION</h2>
   <p class="abs body about-text" style="left:76px;top:374px;width:312px">We are full service general contractor. We service apartment complexes with small and full remodeling projects. We have a rapid response team for urgent needs and have relationship services that offer fixed pricing for most services and estimate pricing for larger and more complex solutions.</p>
   <div class="abs btn about-text" style="left:76px;top:443px;width:71px;height:14px">View Projects</div>
  </section>

  <section>
   <div class="abs services-band" role="img" aria-label="Blurred photo of a furnished living room"></div>
   <div class="abs card" style="left:77px"><div class="ic"><svg width="14" height="14" viewBox="0 0 14 14"><path d="M2 7L7 2l5 5M3.5 6v6h7V6" fill="none" stroke="#c4141a" stroke-width="1.4"/></svg></div><h3>Exterior Renovation<br>and Remodeling</h3><p>Sed ornare ex vel enim venenatis finibu vestibulum sed ornare</p><div class="more"><span>VIEW MORE</span><span>&gt;</span></div></div>
   <div class="abs card" style="left:215px"><div class="ic"><svg width="14" height="14" viewBox="0 0 14 14"><rect x="3" y="2" width="8" height="5" fill="none" stroke="#c4141a" stroke-width="1.4"/><path d="M3 7v5M11 7v5M6 9h5" stroke="#c4141a" stroke-width="1.4"/></svg></div><h3>Interior Renovation<br>and Remodeling</h3><p>Sed ornare ex vel enim venenatis finibu vestibulum sed ornare</p><div class="more"><span>VIEW MORE</span><span>&gt;</span></div></div>
   <div class="abs card blue" style="left:353px"><div class="ic"><svg width="14" height="14" viewBox="0 0 14 14"><rect x="2" y="4" width="10" height="8" fill="#1a4fd8"/><rect x="5" y="2" width="4" height="2" fill="none" stroke="#1a4fd8"/></svg></div><h3>Maintenance<br>Services</h3><p>Sed ornare ex vel enim venenatis finibu vestibulum sed ornare</p><div class="more"><span>VIEW MORE</span><span>&gt;</span></div></div>
   <div class="abs card" style="left:491px"><div class="ic"><svg width="14" height="14" viewBox="0 0 14 14"><circle cx="7" cy="5" r="2.5" fill="#c4141a"/><path d="M3 12h8L9 7H5z" fill="#c4141a"/></svg></div><h3>Project Management<br>and Consulting</h3><p>Sed ornare ex vel enim venenatis finibu vestibulum sed ornare</p><div class="more"><span>VIEW MORE</span><span>&gt;</span></div></div>
  </section>

  <section>
   <div class="abs stat" style="left:39px"><b>46.614</b><span>Satisfied customers</span></div>
   <div class="abs vdiv" style="left:240px"></div>
   <div class="abs stat" style="left:239px"><b>32.439</b><span>Designed floorplans</span></div>
   <div class="abs vdiv" style="left:438px"></div>
   <div class="abs stat" style="left:442px"><b>2.312.67</b><span>Completed projects</span></div>
  </section>

  <nav class="abs cats" role="img" aria-label="Row of dark photo tiles showing each trade">
   <div style="background:#5d5f63">Painting</div><div style="background:#4a3a30">Roofing</div><div style="background:#3e2e25">Bathrooms</div><div style="background:#4d3a2d">Cabinets</div><div style="background:#5a4535">Flooring</div><div style="background:#3a2c24">Kitchens</div><div style="background:#4b4540">Electrical &amp;<br>Plumbing</div><div style="background:#51382a">Door Kick-ins</div><div style="background:#3d2f26">Carpentry</div>
  </nav>

  <section>
   <div class="abs blog"></div>
   <h2 class="abs h2" style="left:76px;top:866px">DESIGN . REMODEL . MAINTENANCE</h2>
   <article class="abs post" style="left:77px"><div class="ph" role="img" aria-label="Photo of a wooden kitchen counter with stovetop" style="background:linear-gradient(180deg,#e8e6e2 0%,#c99a6a 60%,#8a5a35 100%)"></div><h4>Mauris lectus sem, ornare ac eleifend nec, viverra vel elit.</h4><time>November 3, 2016</time><div class="rm"><span>READ MORE</span><span>&gt;</span></div></article>
   <article class="abs post" style="left:262px"><div class="ph" role="img" aria-label="Photo of a modern kitchen with glass cabinets" style="background:linear-gradient(90deg,#f0efec 0%,#2c2420 55%,#a5532a 100%)"></div><h4>Mauris lectus sem, ornare ac eleifend nec, viverra vel elit.</h4><time>November 3, 2016</time><div class="rm"><span>READ MORE</span><span>&gt;</span></div></article>
   <article class="abs post" style="left:447px"><div class="ph" role="img" aria-label="Photo of a carved wood table in a dark room" style="background:linear-gradient(90deg,#2a3340 0%,#8a5a36 50%,#2b2f3a 100%)"></div><h4>Mauris lectus sem, ornare ac eleifend nec, viverra vel elit.</h4><time>November 3, 2016</time><div class="rm"><span>READ MORE</span><span>&gt;</span></div></article>
  </section>

  <section>
   <div class="abs sat" role="img" aria-label="Photo of a warm lit hallway with wall lamps"></div>
   <p class="abs sat-kicker">WE BUILD SATISFACTION</p>
   <h2 class="abs sat-title">AFFORDABLE SOLUTIONS FOR<br>BETTER LIVING</h2>
   <p class="abs sat-copy">Most of the time, we provide all of the necessary materials, but you can purchase materials too if you want. We then give you a timeframe in which we feel we can complete the project. Customers really love our finished product, and you can rest assured that we do the job right the first time. <b>Contact us today</b> for quality remodeling services and excellent discounts.</p>
   <div class="abs btn" style="left:76px;top:1246px;width:71px;height:14px">Learn More</div>
   <div class="abs say">
    <h3 style="margin-top:37px;font-family:'Ubuntu',sans-serif;font-weight:500;font-size:11.5px">WHAT PEOPLE SAY</h3>
    <div role="img" aria-label="Portrait photo of a client" style="width:64px;height:64px;border-radius:50%;margin:10px auto 0;border:2px solid #fff;background:linear-gradient(180deg,#cfd3d8,#8b8f96)"></div>
    <p style="margin:14px 13px 0;font-size:5.5px;line-height:10px">“ Consectetur adipiscing elit. Proin gravida urna sapien, at scelerisque tellus imperdiet eget. Maecenas a mauris eget dolor volutpat porttitor. Etiam tempor nisl imperdiet ultrices hendrerit. Sed vel rhoncus lacus. Nunc aliquam justo quis justo hendrerit. ”</p>
    <p style="margin-top:20px;font-family:'Playfair Display',serif;font-style:italic;font-size:11px">Marcus R. Ellery</p>
   </div>
   <div class="abs sat-right" role="img" aria-label="Dark interior photo"></div>
  </section>

  <footer>
   <nav class="foot-nav"><a style="left:138px">Roofing</a><a style="left:205px">Apartment</a><a style="left:281px">Client Portal</a><a style="left:370px">Services</a><a style="left:437px">Projects</a><a style="left:507px">Contact Us</a></nav>
   <div class="abs" style="left:76px;top:1426px;width:540px;height:1px;background:#bbb"></div>
   <div class="abs social" style="left:210px"></div><div class="abs social" style="left:232px"></div><div class="abs social" style="left:254px"></div><div class="abs social" style="left:276px"></div><div class="abs social" style="left:298px"></div><div class="abs social" style="left:321px"></div>
   <div class="abs" style="left:356px;top:1444px;width:84px;height:17px;border:1px solid #ddd;font-size:5px;color:#999;padding:5px 4px">Email Address</div>
   <div class="abs" style="left:440px;top:1444px;width:43px;height:17px;background:#ddd;font-size:5px;color:#333;text-align:center;line-height:17px">SUBSCRIBE</div>
   <div class="abs copy">© 2016 TALL PINE CONSTRUCTION — All Rights Reserved</div>
  </footer>
 </main>
</div>
</body>
</html>
```